Office brochure for chronic pain doctor

I need an brochure for my office, and since I want to be able to mail the brochure, I think trifold would be the best size. I treat patients with chronic head and neck pain, as well as sleep apnea. I treat all of the following:

1. headaches
2. myofascial pain, which is a fancy way of saying muscle pain
3. neuropathic pain, which is a fancy way of saying nerve pain
4. TMJ, which stands for the temporomandibular joint (jaw joint)
5. obstructive sleep apnea

The colors will be based on my logo on my website, which you can see at www.BrightJPR.net, and you can learn more about what I do at my website. JPR stands for orofacial pain, which is a speciality training within the field of dentistry but I do not treat teeth. I have high resolution graphics for the brochure so I need someone with an artistic eye to design and lay out the brochure.

The logo colors are:
Purple 9e80bb
Pink f6b1d0
Blue 0f4b8f
Updates

I had a request for the logo in a .ai or .pdf format, which I have just uploaded. Please let me know if you have any other requests. Thank you, Dale

Target Market(s)

80% female, 20% male. I am in an upscale area of Los Angeles called Beverly Hills but I will see a patient from any area around Los Angeles or from any area in the world.

Industry/Entity Type

Training

Colors
6b449b
e567a6
0355a3

Requirements
Must have
• I want a small section of the brochure to feature each of the five areas I treat, and I have included an image to place in each of the five sections. A small section should include a short bio of me, which you can condense from www.brightjpr.net/dale. The brochure must appeal to women since 80% of my patients are female but I don't want to completely ignore men. Most of the pain patients are female, and most of the sleep apnea patients are male.

Here are the colors in my logo
Purple 9e80bb
Pink f6b1d0
Blue 0f4b8f
Should not have
• Anything related to teeth or dentistry.
No decorative or script fonts.

```html
<!DOCTYPE html>
<html lang="en">
<head>
<meta charset="utf-8">
<title>Dale — Head, Face &amp; Sleep Care Brochure</title>
<link href="https://fonts.googleapis.com/css2?family=Arimo:wght@400&display=swap" rel="stylesheet">
<style>
  :root {
    --purple: #6b449b;
    --purple-light: #9b80bb;
    --pink: #e567a6;
    --pink-light: #e48db8;
    --blue: #0355a3;
    --blue-light: #4f7ab8;
    --divider: #222;
    --paper: #ffffff;
    --image-tone-top: #ecd6c6;
    --image-tone-bottom: #dcbba5;
  }
  * { box-sizing: border-box; margin: 0; padding: 0; }
  html, body { width: 1200px; height: 849px; overflow: hidden; background: var(--paper); }
  body { font-family: "Arimo", Arial, sans-serif; }
  .brochure { position: relative; width: 1200px; height: 849px; background: var(--paper); overflow: hidden; }
  .panel-divider { position: absolute; top: 0; width: 1px; height: 849px; background: var(--divider); }
  .band { position: absolute; width: 400px; height: 145px; }
  .band__main { height: 120px; }
  .band__accent { height: 25px; }
  .band--purple .band__main { background: var(--purple); }
  .band--purple .band__accent { background: var(--purple-light); }
  .band--pink .band__main { background: var(--pink); }
  .band--pink .band__accent { background: var(--pink-light); }
  .band--blue .band__main { background: var(--blue); }
  .band--blue .band__accent { background: var(--blue-light); }
  .band__title {
    position: absolute; left: 23px; color: #fff; font-size: 26px; font-weight: 400; line-height: 1;
  }
  .topic-image {
    position: absolute; width: 200px; height: 200px; border-radius: 50%;
    border: 6px solid var(--purple-light); background: #fff; padding: 4px;
  }
  .topic-image--pink { border-color: var(--pink-light); }
  .topic-image--blue { border-color: var(--blue-light); }
  .topic-image__fill {
    width: 100%; height: 100%; border-radius: 50%;
    background: linear-gradient(180deg, var(--image-tone-top), var(--image-tone-bottom));
  }
  .copy { position: absolute; font-size: 14.7px; line-height: 18.8px; }
  .copy p + p { margin-top: 18.8px; }
  .copy--purple { color: var(--purple); }
  .copy--pink { color: var(--pink); }
  .copy--blue { color: var(--blue); }
</style>
</head>
<body>
<main class="brochure">

  <section class="panel panel--left">
    <div class="band band--purple" style="left:0; top:0;">
      <div class="band__main"></div><div class="band__accent"></div>
      <h2 class="band__title" style="top:16px;">Haedaches</h2>
    </div>
    <div class="topic-image" style="left:101px; top:29px;">
      <div class="topic-image__fill" role="img" aria-label="Illustration of a headache sufferer with the pain area highlighted"></div>
    </div>
    <div class="copy copy--purple" style="left:12px; top:245px; width:377px;">
      <p>A headache is an ache or pain occurring anywhere in the face, neck or head. Headache pain is experienced through pain-sensitive structures around the head and neck including blood vessels, nerves, muscles and tissues including the eyes, ears and sinuses.</p>
      <p>If you suffer from frequent headaches, finding out the type of headache causing the majority of symptoms is a critical part of treating the underlying causes of the pain. Learn about the major causes, symptoms and treatments for various headache types here, and consult Dr. Halvorsen before starting a treatment plan.</p>
    </div>

    <div class="band band--pink" style="left:0; top:515px;">
      <div class="band__main"></div><div class="band__accent"></div>
      <h2 class="band__title" style="top:9px;">Myofascial pain</h2>
    </div>
    <div class="topic-image topic-image--pink" style="left:101px; top:558px;">
      <div class="topic-image__fill" role="img" aria-label="Anatomical illustration of head and neck muscles"></div>
    </div>
    <div class="copy copy--pink" style="left:12px; top:771px; width:385px;">
      <p>Chronic myofascial pain (CMP) is a chronic pain disease characterized by trigger points in the musculature causing pain in distinct areas of the body.</p>
    </div>
  </section>

  <div class="panel-divider" style="left:400px;"></div>

  <section class="panel panel--middle">
    <div class="copy copy--pink" style="left:409px; top:11px; width:386px;">
      <p>Pain symptoms of CMP can be severe and debilitating. While much of the underlying mechanics of myofascial pain is not clearly understood, research suggests that symptoms are derived from the existence of trigger points within muscles, which are activated by injury or repetitive strain to muscles.</p>
      <p>Chronic myofascial pain symptoms can be mistaken for a large number of other disorders, so a thorough physical examination is required for proper diagnosis of this largely not understood disease.</p>
      <p>Chronic myofascial pain is a complex but manageable disease. Professional attention can help narrow down the causes of chronic pain and make a positive diagnosis of CMP based on physical examination and additional procedures to rule out alternative sources of a patient's pain symptoms.</p>
    </div>

    <div class="band band--blue" style="left:401px; top:380px;">
      <div class="band__main"></div><div class="band__accent"></div>
      <h2 class="band__title" style="top:10px;">Neuropathic pain</h2>
    </div>
    <div class="topic-image topic-image--blue" style="left:498px; top:420px;">
      <div class="topic-image__fill" role="img" aria-label="Illustration of facial nerve branches and pain distribution"></div>
    </div>
    <div class="copy copy--blue" style="left:409px; top:637px; width:388px;">
      <p>Neuropathic pain disorders are a set of pain conditions resulting from disorder or injury to the nervous system. The human nervous system is divided into two general parts: the central nervous system, comprising the brain and spinal cord, and the peripheral nervous system, including nerves that go to the limbs, trunk, face and all outlying areas of the body.</p>
      <p>Additionally, the spine and brain command a network a nerves conducting sensation along the back, neck,</p>
    </div>
  </section>

  <div class="panel-divider" style="left:800px;"></div>

  <section class="panel panel--right">
    <div class="copy copy--blue" style="left:810px; top:11px; width:382px;">
      <p>head and face.When nerves of the peripheral system sense pain from mechanical, chemical or thermal sensations, they relay the sensation to the central nervous system for processing.Damage to nerves of the peripheral or central nervous system can cause pain signals to be sent to the brain, which may result in the chronic pain condition known as neuropathic pain.</p>
      <p>Neuropathic orofacial pain conditions refer to those with symptoms that primarily affect a patient's mouth and face.&nbsp; Orofacial means of the mouth or face.</p>
    </div>

    <div class="band band--purple" style="left:801px; top:257px;">
      <div class="band__main"></div><div class="band__accent"></div>
      <h2 class="band__title" style="top:9px;">Obstructive sleep apnea</h2>
    </div>
    <div class="topic-image" style="left:900px; top:292px;">
      <div class="topic-image__fill" role="img" aria-label="Illustration of a sleeper with the airway shown in cross-section"></div>
    </div>
    <div class="copy copy--purple" style="left:810px; top:506px; width:382px;">
      <p>Sleep apnea is a common sleeping disorder marked by shallow breathing, pauses in breath and labored breathing punctuated by gasping or snoring sounds. A pause may be followed by a choking or snorting sound as the sleeper involuntarily gasps for breath.</p>
      <p>A person suffering from sleep apnea finds himself or herself tired during the day as the disorder inhibits restful sleep. A lack of quality sleep can lead to accidents or poor job performance. Serious health concerns including heart disease, high blood pressure, stroke, diabetes and depression can also result from untreated sleep apnea.</p>
      <p>The condition is a highly manageable one as there are a number of treatment options that can relieve the symptoms of sleep apnea.</p>
    </div>
  </section>

</main>
</body>
</html>
```